Website for peer to peer car sharing service

Hi all,

We need a web design for a new environmental friendly peer-to-peer car sharing website.

The website will serve as a marketplace where car owners can list their car and drivers that who do not have access to a car can rent a suitable car. It is important for us to emphasis that this is a community where the main purpose is to use the vehicles on the street in a more efficient way.

Attached are five pictures where we have sketched up the five main pages:

File 1. Info site for a particular car.
File 2. Logo.
File 3. Register a car.
File 4. Sign up.
File 5. Search.
File 6. Front page.

The logo for the company is attached (File 2) and it would be ideal to design the website in relation to the logo. The final design should relate to a secure market place which is environmental friendly.

We would like this webpage to be in the same spirit as www.velnoro.it, www.brundale.com, www.plimtrovesite.com, https://wend.kul.net, https://garbelow.com etc.

We look forward to see your designs.

Best regards,
The Trundo Team.

Hi guys, 

Please take :

1) Could you please design icons for for  'FAQ' and 'Insurance' in the header, locate the icons right to the Trundo logo. We only want two icons ('FAQ' and 'Insurance')  right to the Trundo logo.

2) The height of the header should be the same as the header of faplex.com

3) The price tags for the cars (below the top section) should be similar to the price tags at mostanbee.com.

4) We would like you to start to design the other pages (the sub-pages listed in the project description:
a)Info site for a particular car.
b)Register a car. 
c)Search results (similar to http://www.pevrotank.com/find-car).

Please take a look at the picture attached for the sub-pages:

https://files.quenmolt.example/brief_uploads/000001_3_search_000001_brief000001.jpg

https://files.quenmolt.example/brief_uploads/000002_4_infositeforaparticularcar_000002_brief000002.jpg

http://www.quenmolt.example/file.aspx?fileLocation=storage_url/brief_uploads/000003_5_registeracar_brief000003.jpg

Best regards, 
Trundo team 

Target Market(s)

The target market are people from 20-40 years old who are environmental friendly, also tourists who visit the city and would like to rent a car.

Industry/Entity Type

It Company

Requirements
Must have
• It is required that the designer that will be chosen will hand in layered PSD files of each web page.

```html
<!DOCTYPE html>
<html lang="en">
<head>
<meta charset="utf-8">
<title>Trundo – Car Details</title>
<link href="https://fonts.googleapis.com/css2?family=Figtree:wght@400;500;600;700&family=Arimo:wght@400;700&family=Oswald:wght@500&display=swap" rel="stylesheet">
<style>
:root{
  --header-dark:#1c1c1c;
  --brand-green:#7dc242;
  --title-green:#4f9a16;
  --btn-green-top:#8fd13a;
  --btn-green-bottom:#4c9b12;
  --ink:#111;
  --body-text:#444;
  --rule:#dcdcdc;
  --panel:#efefef;
  --panel-line:#e2e2e2;
  --gallery:#333;
  --star:#f5c400;
  --price-red:#e8141b;
  --footer:#262626;
}
*{margin:0;padding:0;box-sizing:border-box}
html,body{width:1200px;height:1126px;overflow:hidden}
body{position:relative;background:#fff;font-family:"Figtree",Arial,sans-serif;color:var(--ink)}
.abs{position:absolute}

/* header */
.site-header{left:0;top:0;width:1200px;height:103px;background:linear-gradient(#2b2b2b,var(--header-dark))}
.header-accent{left:0;top:103px;width:1200px;height:4px;background:var(--brand-green)}
.header-shade{left:0;top:107px;width:1200px;height:60px;background:linear-gradient(#e6e6e6,#fff)}
.brand{left:131px;top:22px;display:flex;align-items:center;gap:14px}
.brand-dot{width:44px;height:44px;border-radius:50%;background:var(--brand-green)}
.brand-name{font-weight:700;font-size:50px;color:#fff;line-height:1}
.auth-btn{top:36px;height:26px;border-radius:13px;background:linear-gradient(#fff,#dcdcdc);display:flex;align-items:center;gap:6px;padding:0 10px;font-weight:600;font-size:15px;color:#111}
.auth-btn svg{width:14px;height:14px}
.btn-register{left:864px;width:110px}
.btn-login{left:984px;width:83px}

/* media tabs */
.media-tabs{left:131px;top:131px;width:122px}
.media-tab{height:40px;display:flex;align-items:center;gap:9px;padding-left:10px;background:#e4e4e4;font-weight:500;font-size:15px;color:#555;letter-spacing:.3px}
.media-tab.is-active{background:var(--gallery);color:#fff}
.media-tab svg{width:15px;height:15px}
.gallery{left:253px;top:131px;width:507px;height:397px;background:var(--gallery)}
.gallery-main{left:263px;top:140px;width:487px;height:305px;background:radial-gradient(ellipse at 50% 55%,#d9262a 0,#c81d22 28%,#f3e6e6 52%,#fff 70%)}
.thumb{top:454px;width:90px;height:66px}

/* content */
.rule{left:131px;width:629px;height:1px;background:var(--rule)}
.section-title{font-weight:500;font-size:22px;color:var(--title-green)}
.about-title{left:131px;top:562px}
.copy{font-size:13.5px;line-height:20.5px;color:var(--body-text);white-space:nowrap}
.about-copy{left:131px;top:597px}
.reviews-title{left:131px;top:702px;font-weight:500;font-size:21px;color:var(--ink)}
.stat{font-weight:500;font-size:18px;color:var(--ink)}
.rating-row{display:flex;align-items:center;gap:10px;font-size:13.5px;color:#555}
.stars{display:flex;gap:3px}
.stars svg{width:17px;height:17px;fill:var(--star)}
.avatar{left:131px;top:901px;width:74px;height:75px;border:3px solid #e8e8e8;background:#000}
.review-name{left:224px;top:900px;font-weight:500;font-size:18px}
.review-date{right:442px;top:900px;font-weight:600;font-size:17px}
.review-copy{left:224px;top:933px}

/* booking panel */
.booking{left:787px;top:131px;width:281px;height:476px;background:var(--panel);border:1px solid var(--panel-line)}
.price-option{position:absolute;left:0;width:279px;height:52px;border-bottom:2px solid #fafafa;display:flex;align-items:center;gap:14px;padding-left:18px;font-weight:600;font-size:16px;color:#111}
.checkbox{width:13px;height:13px;border:1px solid #aaa;background:#fff;display:flex;align-items:center;justify-content:center}
.field-label{font-size:16px;color:#111}
.select{height:32px;border:1px solid #ccc;background:#fff;box-shadow:inset 0 0 0 2px #f5f5f5;display:flex;align-items:center;justify-content:space-between;padding:0 10px;font-size:14px;color:#888}
.select::after{content:"";border:4px solid transparent;border-top:5px solid #666;margin-top:5px}
.subtotal{left:801px;top:472px;font-weight:700;font-size:23px}
.subtotal span{color:var(--price-red)}
.book-btn{left:802px;top:524px;width:246px;height:64px;border-radius:3px;background:linear-gradient(var(--btn-green-top),var(--btn-green-bottom));display:flex;align-items:center;justify-content:center;gap:16px;font-family:"Oswald",sans-serif;font-weight:500;font-size:42px;color:#fff;letter-spacing:1px}

/* owner */
.owner-panel{left:787px;top:636px;width:281px;height:420px;background:var(--panel)}
.owner-head{left:787px;top:636px;width:281px;height:54px;background:linear-gradient(#555,#1e1e1e);color:#fff;font-weight:500;font-size:22px;padding:14px 0 0 17px}
.owner-photo{left:802px;top:706px;width:253px;height:172px;background:linear-gradient(#111,#000)}
.owner-name{left:801px;top:888px;font-weight:500;font-size:18px}
.info-label{display:flex;align-items:center;gap:9px;font-weight:600;font-size:14px}
.info-label svg{width:13px;height:15px}
.info-text{font-size:13.5px;line-height:21px;color:#444}

/* footer */
.site-footer{left:0;top:1082px;width:1200px;height:44px;background:var(--footer);color:#ccc;font-size:13.5px}
.site-footer .left{left:131px;top:13px}
.site-footer .right{right:133px;top:13px}
</style>
</head>
<body>

<header class="abs site-header"></header>
<div class="abs header-accent"></div>
<div class="abs header-shade"></div>
<div class="abs brand"><span class="brand-dot"></span><span class="brand-name">Trundo</span></div>
<a class="abs auth-btn btn-register"><svg viewBox="0 0 14 14"><circle cx="7" cy="4" r="3.2" fill="#111"/><path d="M1 14c0-4 3-6 6-6s6 2 6 6z" fill="#111"/></svg>REGISTER</a>
<a class="abs auth-btn btn-login"><svg viewBox="0 0 14 14"><path d="M4 6V4.5a3 3 0 016 0V6" stroke="#111" stroke-width="1.8" fill="none"/><rect x="2" y="6" width="10" height="8" rx="1" fill="#111"/></svg>LOGIN</a>

<nav class="abs media-tabs">
  <div class="media-tab is-active"><svg viewBox="0 0 15 15"><rect x="1" y="2" width="13" height="11" fill="none" stroke="#fff" stroke-width="1.5"/><path d="M3 11l3-4 2 3 2-2 2 3z" fill="#fff"/></svg>PICTURES</div>
  <div class="media-tab"><svg viewBox="0 0 15 15"><rect x="1" y="2" width="13" height="11" fill="none" stroke="#666" stroke-width="1.3"/><path d="M3 10l3-3 3 2 3-4" stroke="#666" fill="none"/></svg>MAP</div>
  <div class="media-tab"><svg viewBox="0 0 15 15"><rect x="1" y="3" width="13" height="11" fill="#666"/><rect x="3" y="7" width="9" height="5" fill="#e4e4e4"/><rect x="4" y="1" width="2" height="3" fill="#666"/><rect x="9" y="1" width="2" height="3" fill="#666"/></svg>CALENDER</div>
</nav>
<div class="abs gallery"></div>
<div class="abs gallery-main" role="img" aria-label="Photo of the red hatchback car"></div>
<div class="abs thumb" style="left:263px;background:linear-gradient(#fff 20%,#d4262b 45%,#c41e22 70%,#fff 85%)" role="img" aria-label="Car thumbnail, front side view"></div>
<div class="abs thumb" style="left:362px;background:linear-gradient(#fff 20%,#d4262b 45%,#c41e22 70%,#fff 85%)" role="img" aria-label="Car thumbnail, front angle"></div>
<div class="abs thumb" style="left:462px;background:linear-gradient(135deg,#b8181d,#e33a3f 50%,#8b8b8b)" role="img" aria-label="Car thumbnail, wheel detail"></div>
<div class="abs thumb" style="left:561px;background:linear-gradient(#c8141a 10%,#eee 30%,#ddd 80%,#c8141a)" role="img" aria-label="Car thumbnail, door detail"></div>
<div class="abs thumb" style="left:660px;background:linear-gradient(135deg,#ddd,#555 50%,#d21d22)" role="img" aria-label="Car thumbnail, interior seat"></div>

<div class="abs rule" style="top:547px"></div>
<h2 class="abs section-title about-title">About Car Title</h2>
<p class="abs copy about-copy">This is Velmaro's version &nbsp;of Lorem Ipsum. Proin gravida nibh vel velit auctor aliquet. Aenean sollic-<br>itudin, lorem quis bibendum auctor, nisi elit consequat ipsum, nec sagittis sem nibh id elit. Duis sed<br>odio sit amet nibh vulputate cursus a sit amet mauris. Morbi accumsan ipsum velit.</p>

<h2 class="abs reviews-title">Reviews Title</h2>
<div class="abs rule" style="top:743px"></div>
<div class="abs stat" style="left:131px;top:757px">Trips 300</div>
<div class="abs stat" style="left:598px;top:757px">Ratings 150</div>
<svg width="0" height="0" style="position:absolute"><defs><path id="star" d="M8.5 0l2.6 5.4 5.9.8-4.3 4.1 1 5.8-5.2-2.8-5.2 2.8 1-5.8L0 6.2l5.9-.8z"/></defs></svg>
<div class="abs rating-row" style="left:131px;top:799px">Rating<span class="stars"><svg><use href="#star"/></svg><svg><use href="#star"/></svg><svg><use href="#star"/></svg></span></div>
<div class="abs rating-row" style="left:131px;top:828px">Rating<span class="stars"><svg><use href="#star"/></svg><svg><use href="#star"/></svg><svg><use href="#star"/></svg></span></div>
<div class="abs rating-row" style="left:598px;top:799px">Rating<span class="stars"><svg><use href="#star"/></svg><svg><use href="#star"/></svg></span></div>
<div class="abs rating-row" style="left:598px;top:828px">Rating<span class="stars"><svg><use href="#star"/></svg><svg><use href="#star"/></svg><svg><use href="#star"/></svg><svg><use href="#star"/></svg></span></div>
<div class="abs rule" style="top:872px"></div>

<div class="abs avatar" role="img" aria-label="Reviewer profile picture placeholder"></div>
<div class="abs review-name">User Name</div>
<div class="abs review-date">Date : 22/07/2013</div>
<p class="abs copy review-copy">This is Velmaro's version &nbsp;of Lorem Ipsum. Proin gravida nibh vel velit auctor aliquet.<br>Aenean sollicitudin, lorem quis bibendum auctor, nisi elit consequat ipsum, nec sagittis<br>sem nibh id elit. Duis sed odio sit amet nibh vulputate cursus a sit amet mauris. Morbi<br>accumsan ipsum velit. Nam nec tellus a odio tincidunt auctor a ornare odio. Sed non<br>mauris vitae erat consequat auctor eu in elit.</p>

<aside class="abs booking">
  <div class="price-option" style="top:0"><span class="checkbox"><svg width="11" height="11" viewBox="0 0 11 11"><path d="M1.5 5.5l3 3 5-7" stroke="#4f9a16" stroke-width="2" fill="none"/></svg></span>PRIZE PER DAYS</div>
  <div class="price-option" style="top:52px"><span class="checkbox"></span>PRIZE PER HOURS</div>
  <div class="price-option" style="top:104px"><span class="checkbox"></span>PRIZE PER WEEK</div>
</aside>
<div class="abs field-label" style="left:801px;top:301px">Start Date</div>
<div class="abs select" style="left:804px;top:332px;width:116px">Date</div>
<div class="abs select" style="left:935px;top:332px;width:116px">Time</div>
<div class="abs field-label" style="left:801px;top:383px">End Date</div>
<div class="abs select" style="left:804px;top:413px;width:116px">Date</div>
<div class="abs select" style="left:935px;top:413px;width:116px">Time</div>
<div class="abs subtotal">SUB TOTAL <span>$ 200</span></div>
<a class="abs book-btn"><svg width="64" height="36" viewBox="0 0 64 36"><path d="M4 22l4-10c1-3 3-4 6-4h30c3 0 5 1 7 4l6 8c3 0 5 2 5 5v4H4z" fill="#fff"/><rect x="15" y="11" width="13" height="8" fill="#6bb82a"/><rect x="31" y="11" width="14" height="8" fill="#6bb82a"/><circle cx="16" cy="29" r="6" fill="#fff" stroke="#6bb82a" stroke-width="2.5"/><circle cx="48" cy="29" r="6" fill="#fff" stroke="#6bb82a" stroke-width="2.5"/></svg>BOOK IT</a>

<div class="abs owner-panel"></div>
<div class="abs owner-head">Owner Info</div>
<div class="abs owner-photo" role="img" aria-label="Car owner profile picture placeholder"></div>
<div class="abs owner-name">Owners Name</div>
<div class="abs info-label" style="left:801px;top:924px"><svg viewBox="0 0 13 15"><path d="M6.5 1a4.5 4.5 0 00-4.5 4.5c0 3.5 4.5 8.5 4.5 8.5s4.5-5 4.5-8.5A4.5 4.5 0 006.5 1z" fill="none" stroke="#555" stroke-width="1.4"/><circle cx="6.5" cy="5.5" r="1.6" fill="#555"/></svg>Location :</div>
<div class="abs info-text" style="left:801px;top:946px">22, Stress address, Cityname,<br>886 Country</div>
<div class="abs info-label" style="left:801px;top:1004px"><svg viewBox="0 0 13 15"><rect x="3" y="1" width="7" height="13" rx="1.2" fill="none" stroke="#555" stroke-width="1.4"/><circle cx="6.5" cy="11.5" r=".9" fill="#555"/></svg>Phone :</div>
<div class="abs info-text" style="left:801px;top:1024px">(012) 888. 9999. 1234</div>

<footer class="abs site-footer">
  <span class="abs left">Copyright © 2013 Trundo. All Rights Reserved.</span>
  <span class="abs right">Powered By : Wexlor Studio Pvt Ltd.</span>
</footer>

</body>
</html>
```